Wordpress Design For Virtual Assistant

I need a website design for my virtual assistant company, BrimLoop. I would like to have a landing page, an about page, a page to list my services, contact us and FAQ. a blog page would be great as well.

It needs to be a modern, professional but fun look. Simple and easy to read and navigate. Colors used need to match the logo colors exactly with the red color being used only as a highlight/accept color.

I have uploaded an overview of BrimLoop as well as my logo, copy of business card and stationary to give you an idea of the design style I prefer.

Industry/Entity Type

It Company

Coding

Coded - Design and coding required

Font styles to use
Sans Serif

Requirements
Must have
• Color scheme with exact logo colors
Nice to have
• www.quorvane.com/ can be used as an style inspiration

```html
<!DOCTYPE html>
<html lang="en">
<head>
<meta charset="utf-8">
<title>BrimLoop – Virtual Assistant</title>
<link href="https://fonts.googleapis.com/css2?family=Open+Sans:wght@400;600;700;800&display=swap" rel="stylesheet">
<style>
:root{
  --green:#6fa91b;
  --red:#bc311d;
  --teal:#368a97;
  --ink:#2b2b2b;
  --body:#555;
  --light:#f1f1f1;
  --footer:#1f1f1f;
  --white:#fff;
}
*{margin:0;padding:0;box-sizing:border-box}
html,body{width:1200px;height:2659px;overflow:hidden}
body{font-family:"Open Sans",Arial,sans-serif;color:var(--ink);background:var(--white);position:relative}
.abs{position:absolute}
.tribar{position:absolute;left:0;width:1200px;height:5px;display:flex;gap:3px}
.tribar span{flex:1}
.tribar .g{background:var(--green)}.tribar .r{background:var(--red)}.tribar .t{background:var(--teal)}
.tribar.bottom{top:2646px;height:13px}

/* header */
.site-header{position:absolute;top:0;left:0;width:1200px;height:94px}
.brand{position:absolute;left:164px;top:30px;font-size:34px;font-weight:800;color:var(--ink);letter-spacing:-1px}
.phone{position:absolute;left:778px;top:16px;color:var(--red);font-size:19px;display:flex;align-items:center;gap:6px}
.search{position:absolute;left:923px;top:17px;width:114px;height:25px;border:1px solid #ccc;display:flex}
.search span{flex:1;font-size:11px;color:#666;padding:5px 8px}
.search i{width:25px;background:#888;display:flex;align-items:center;justify-content:center}
.main-nav{position:absolute;top:58px;left:622px;display:flex;gap:0;font-size:12.5px}
.main-nav a{color:var(--ink);text-decoration:none;padding:4px 12px;margin-right:4px}
.main-nav a.active{background:var(--red);color:var(--white);border-radius:5px;padding:4px 17px;margin-right:14px}

/* hero */
.hero{position:absolute;top:94px;left:0;width:1200px;height:480px;background:linear-gradient(100deg,#5b5652 0%,#6e6a66 30%,#8d8c8a 60%,#bfc2c3 85%,#e2e3e3 100%)}
.hero-copy{position:absolute;top:242px;width:1200px;text-align:center;color:var(--white)}
.hero-copy h1{font-size:39px;font-weight:800;letter-spacing:.5px;line-height:1}
.hero-copy p{font-size:23px;margin-top:4px}
.btn{display:inline-flex;align-items:center;gap:10px;background:var(--red);color:var(--white);font-weight:700;font-size:11.5px;letter-spacing:2px;border-radius:3px;text-decoration:none}
.hero .btn{position:absolute;left:525px;top:330px;width:150px;height:32px;justify-content:center}
.dots{position:absolute;top:424px;left:533px;display:flex;gap:22px;align-items:center}
.dots span{width:9px;height:9px;border-radius:50%;background:var(--white)}
.dots span.on{width:15px;height:15px;background:none;border:2px solid var(--white)}

/* section titles */
.sec-title{position:absolute;width:1200px;text-align:center;font-size:23px;font-weight:600;color:var(--ink)}
.sec-title::after{content:"";display:block;width:58px;height:2px;background:var(--ink);margin:6px auto 0}

/* welcome */
.welcome-text{position:absolute;left:278px;top:652px;width:646px;text-align:center;font-size:12.5px;line-height:19px;color:var(--body)}
.tile{position:absolute;top:728px;height:164px;color:var(--white);text-align:center;font-size:18px}
.tile svg{display:block;margin:28px auto 18px}
.tile.green{left:278px;width:211px;background:var(--green)}
.tile.red{left:496px;width:210px;background:var(--red)}
.tile.teal{left:713px;width:211px;background:var(--teal)}

/* services */
.services{position:absolute;top:920px;left:0;width:1200px;height:457px;background:linear-gradient(180deg,#e4e4e4,#d6d6d6 60%,#cfcfcf)}
.service{position:absolute;width:280px;text-align:center}
.service svg{display:block;margin:0 auto}
.service h3{font-size:15.5px;font-weight:700;margin-top:8px}
.service p{font-size:11.5px;line-height:17px;color:#555;margin-top:6px}
.c-green{color:var(--green)}.c-red{color:var(--red)}.c-teal{color:var(--teal)}
.divider{position:absolute;top:1030px;width:1px;height:310px;background:#c4c4c4}

/* owners */
.owners-photo{position:absolute;left:53px;top:1385px;width:372px;height:320px;background:linear-gradient(90deg,#f4f4f4,#cfc6c0 40%,#8a6f63 60%,#e9e9e9)}
.owners-copy{position:absolute;left:441px;top:1453px;width:529px;text-align:center}
.owners-copy h2,.entre-copy h2{font-size:21px;font-weight:600}
.owners-copy p,.entre-copy p{font-size:11.5px;line-height:19px;color:#444;margin-top:14px}
.owners-copy .btn,.entre-copy .btn{height:32px;width:152px;justify-content:center;margin-top:22px}

/* entrepreneurs */
.entre-bg{position:absolute;left:0;top:1705px;width:757px;height:310px;background:linear-gradient(90deg,#ececec,#f7f7f7 50%,#e3e5e6)}
.entre-photo{position:absolute;left:757px;top:1705px;width:443px;height:310px;background:linear-gradient(120deg,#f2f2f2,#b9bbbd 40%,#5e6670 65%,#d9dadb)}
.entre-copy{position:absolute;left:168px;top:1786px;width:479px;text-align:center}

/* blog */
.blog{position:absolute;top:2015px;left:0;width:1200px;height:406px;background:#e9e9e9}
.card{position:absolute;top:2118px;width:281px;height:257px;background:var(--white)}
.card .img{height:156px;background:linear-gradient(135deg,#5d5a56,#a9a39c)}
.card .date{position:absolute;right:0;top:-8px;width:34px;height:34px;border-radius:50%;background:#3a3a3a;color:var(--white);text-align:center;font-size:13px;font-weight:700;line-height:13px;padding-top:7px;border:2px solid #e9e9e9}
.card .date small{display:block;font-size:7px}
.card h4{font-size:12.5px;font-weight:700;margin:12px 18px 0}
.card p{font-size:11.5px;line-height:18px;color:#555;margin:3px 18px 0}
.card .more{position:absolute;right:0;bottom:0;background:var(--red);color:var(--white);font-size:8.5px;font-weight:700;padding:3px 8px}

/* footer */
.site-footer{position:absolute;top:2421px;left:0;width:1200px;height:225px;background:var(--footer);color:#ddd}
.f-col{position:absolute;top:36px;font-size:10.5px}
.f-col h5{font-size:11.5px;font-weight:700;color:var(--white);margin-bottom:12px}
.f-col li{list-style:none;line-height:18px}
.f-contact li{display:flex;gap:12px;align-items:flex-start}
.f-contact svg{margin-top:4px;flex:none}
.email-field{width:158px;height:32px;background:#3a3a3a;border-radius:3px;font-size:10px;color:#ccc;display:flex;align-items:center;gap:8px;padding-left:12px}
.signup{width:158px;height:33px;background:var(--red);border-radius:3px;color:var(--white);font-weight:800;font-size:15px;text-align:center;line-height:33px;margin-top:15px}
.f-brand{position:absolute;left:918px;top:72px;font-size:34px;font-weight:800;color:var(--white);letter-spacing:-1px}
.copyright{position:absolute;left:870px;top:193px;font-size:9.5px;color:#ccc}
</style>
</head>
<body>

<div class="tribar"><span class="g"></span><span class="r"></span><span class="t"></span></div>

<header class="site-header">
  <div class="brand">BrimLoop</div>
  <div class="phone">
    <svg width="14" height="14" viewBox="0 0 24 24"><path fill="var(--red)" d="M6.6 10.8a15 15 0 0 0 6.6 6.6l2.2-2.2c.3-.3.7-.4 1-.2 1.1.4 2.3.6 3.6.6.6 0 1 .4 1 1V20c0 .6-.4 1-1 1A17 17 0 0 1 3 4c0-.6.4-1 1-1h3.5c.6 0 1 .4 1 1 0 1.3.2 2.5.6 3.6.1.3 0 .7-.2 1z"/></svg>
    (555) 014 2290
  </div>
  <div class="search"><span>Search</span><i><svg width="11" height="11" viewBox="0 0 24 24"><circle cx="10" cy="10" r="6.5" fill="none" stroke="#fff" stroke-width="3"/><path d="M15 15l6 6" stroke="#fff" stroke-width="3"/></svg></i></div>
  <nav class="main-nav">
    <a class="active">Home</a><a>About us</a><a>Services</a><a>FAQ</a><a>Blog</a><a>Contact us</a>
  </nav>
</header>

<section class="hero" role="img" aria-label="Photo of a team working at computers in a bright office">
  <div class="hero-copy">
    <h1>VIRTUAL ASSISTANT</h1>
    <p>small business owners &amp; entrepreneurs</p>
  </div>
  <a class="btn">LEARN MORE <svg width="18" height="8" viewBox="0 0 18 8"><path d="M0 4h15M12 1l4 3-4 3" stroke="#fff" stroke-width="1.8" fill="none"/></svg></a>
  <div class="dots"><span></span><span class="on"></span><span></span><span></span><span></span></div>
</section>

<h2 class="sec-title" style="top:598px">Welcome to our site</h2>
<p class="welcome-text">BrimLoop provides small business owners &amp; entrepreneurs with critical administrative, and management support, virtually.We offer a comprehensive, affordable way to grow your brand presence and compete with competitors, both large and small, by reaching your market virtually.</p>

<div class="tile green">
  <svg width="44" height="56" viewBox="0 0 44 56"><path d="M22 4a15 15 0 0 0-9 27c2 1.6 3 3.5 3 6h12c0-2.5 1-4.4 3-6A15 15 0 0 0 22 4z" fill="none" stroke="#fff" stroke-width="3.5"/><path d="M16 43h12M17 49h10" stroke="#fff" stroke-width="3.5" stroke-linecap="round"/></svg>
  Operations
</div>
<div class="tile red">
  <svg width="56" height="56" viewBox="0 0 56 56"><g fill="none" stroke="#fff" stroke-width="4" stroke-linecap="round"><path d="M24 20l8-8a7 7 0 0 1 10 10l-8 8a7 7 0 0 1-10 0"/><path d="M32 36l-8 8a7 7 0 0 1-10-10l8-8a7 7 0 0 1 10 0"/></g></svg>
  Marketing
</div>
<div class="tile teal">
  <svg width="60" height="56" viewBox="0 0 60 56"><rect x="4" y="24" width="12" height="28" fill="#fff"/><rect x="24" y="10" width="12" height="42" fill="#fff"/><rect x="44" y="24" width="12" height="28" fill="#fff"/></svg>
  Competition
</div>

<section class="services" role="img" aria-label="Faded photo of a business team in a meeting"></section>
<h2 class="sec-title" style="top:946px">Our Services</h2>
<div class="divider" style="left:441px"></div>
<div class="divider" style="left:762px"></div>

<div class="service" style="left:144px;top:1032px">
  <svg width="44" height="44" viewBox="0 0 44 44"><g fill="none" stroke="var(--green)" stroke-width="2.5"><path d="M10 4h18v36H10z"/><path d="M22 32l12-14 4 3-12 14-5 1z"/></g></svg>
  <h3 class="c-green">Content Creation</h3>
  <p>Lorem Ipsum is simply dummy text of the printing<br>and typesetting industry.</p>
</div>
<div class="service" style="left:457px;top:1032px">
  <svg width="44" height="44" viewBox="0 0 44 44"><g fill="var(--red)"><circle cx="22" cy="7" r="4"/><rect x="18" y="12" width="8" height="7"/><circle cx="9" cy="27" r="3.5"/><circle cx="22" cy="27" r="3.5"/><circle cx="35" cy="27" r="3.5"/><rect x="5" y="31" width="8" height="7"/><rect x="18" y="31" width="8" height="7"/><rect x="31" y="31" width="8" height="7"/></g><path d="M9 23v-3h26v3M22 19v4" stroke="var(--red)" stroke-width="2" fill="none"/></svg>
  <h3 class="c-red">Virtual Organization</h3>
  <p>Lorem Ipsum is simply dummy text of the printing<br>and typesetting industry.</p>
</div>
<div class="service" style="left:775px;top:1032px">
  <svg width="60" height="44" viewBox="0 0 60 44"><g fill="none" stroke="var(--teal)" stroke-width="2.5" stroke-linejoin="round"><path d="M2 14l10-6 8 16-8 5z"/><path d="M58 14l-10-6-8 16 8 5z"/><path d="M14 12l10-4 8 3 10-2 4 13-14 12-14-8z"/></g></svg>
  <h3 class="c-teal">Business Consulting</h3>
  <p>Lorem Ipsum is simply dummy text of the printing<br>and typesetting industry.</p>
</div>

<div class="service" style="left:144px;top:1204px">
  <svg width="44" height="44" viewBox="0 0 44 44"><g fill="none" stroke="var(--green)" stroke-width="2.5"><rect x="4" y="7" width="30" height="28"/><path d="M4 15h30M11 3v7M27 3v7"/><circle cx="33" cy="33" r="8" fill="#ddd"/><path d="M33 29v4h3"/></g></svg>
  <h3 class="c-green">Event Planning</h3>
  <p>Lorem Ipsum is simply dummy text of the printing<br>and typesetting industry.</p>
</div>
<div class="service" style="left:457px;top:1204px">
  <svg width="48" height="44" viewBox="0 0 48 44"><path d="M18 42s-12-13-12-22a12 12 0 0 1 24 0c0 9-12 22-12 22z" fill="var(--red)"/><circle cx="18" cy="20" r="4.5" fill="#ddd"/><path d="M36 22s-7-8-7-13a7 7 0 0 1 14 0c0 5-7 13-7 13z" fill="none" stroke="var(--red)" stroke-width="2.5"/></svg>
  <h3 class="c-red">Travel Arrangements</h3>
  <p>Lorem Ipsum is simply dummy text of the printing<br>and typesetting industry.</p>
</div>
<div class="service" style="left:775px;top:1204px">
  <svg width="48" height="44" viewBox="0 0 48 44"><g fill="none" stroke="var(--teal)" stroke-width="2.5"><rect x="6" y="10" width="36" height="26"/><path d="M6 10l18 14 18-14"/></g></svg>
  <h3 class="c-teal">Blast Mailings</h3>
  <p>Lorem Ipsum is simply dummy text of the printing<br>and typesetting industry.</p>
</div>

<div class="owners-photo" role="img" aria-label="Photo of a smiling businesswoman with crossed arms"></div>
<div class="owners-copy">
  <h2>Small Business Owners</h2>
  <p>There are many variations of passages of Lorem Ipsum available, but the majority have suffered alteration in some form, by injected humour, or randomised words which don't look even slightly believable. If you are going to use a passage of Lorem Ipsum. All the Lorem Ipsum generators on the Internet tend to repeat predefined chunks as necessary, making this the first true generator</p>
  <a class="btn">LEARN MORE <svg width="18" height="8" viewBox="0 0 18 8"><path d="M0 4h15M12 1l4 3-4 3" stroke="#fff" stroke-width="1.8" fill="none"/></svg></a>
</div>

<div class="entre-bg" role="img" aria-label="Pale photo of a modern office interior"></div>
<div class="entre-photo" role="img" aria-label="Photo of a businessman in a suit reading a tablet"></div>
<div class="entre-copy">
  <h2>Entrepreneurs</h2>
  <p>It is a long established fact that a reader will be distracted by the readable content of a page when looking at its layout. The point of using Lorem Ipsum is that it has a more-or-less normal distribution of letters, as opposed to using 'Content here, content here', making it look like readable English. Many desktop publishing packages and web page editors now use Lorem Ipsum.</p>
  <a class="btn">LEARN MORE <svg width="18" height="8" viewBox="0 0 18 8"><path d="M0 4h15M12 1l4 3-4 3" stroke="#fff" stroke-width="1.8" fill="none"/></svg></a>
</div>

<section class="blog"></section>
<h2 class="sec-title" style="top:2050px">Our Blog</h2>

<article class="card" style="left:160px">
  <div class="img" role="img" aria-label="Photo of a man working on a laptop at a cafe"></div>
  <div class="date">05<small>JAN</small></div>
  <h4>Lorem Ipsum is simply dummy</h4>
  <p>It is a long established fact that a reader will be distracted by the readable.</p>
  <span class="more">READ MORE</span>
</article>
<article class="card" style="left:457px">
  <div class="img" role="img" aria-label="Photo of three women looking at a tablet"></div>
  <div class="date">05<small>JAN</small></div>
  <h4>Contrary to popular belief, Lorem Ipsum</h4>
  <p>It is a long established fact that a reader will be distracted by the readable.</p>
  <span class="more">READ MORE</span>
</article>
<article class="card" style="left:753px">
  <div class="img" role="img" aria-label="Illustration of a businessman with digital icons" style="background:linear-gradient(135deg,#1f4a5a,#4f8e98)"></div>
  <div class="date">05<small>JAN</small></div>
  <h4>There are many variations of passages</h4>
  <p>It is a long established fact that a reader will be distracted by the readable.</p>
  <span class="more">READ MORE</span>
</article>

<footer class="site-footer">
  <div class="f-col" style="left:160px">
    <h5>MENU</h5>
    <ul><li>Home</li><li>About us</li><li>Services</li><li>FAQ</li><li>Blog</li><li>Contact us</li></ul>
  </div>
  <div class="f-col" style="left:289px">
    <h5>SERVICES</h5>
    <ul><li>Content Creation/support</li><li>Virtual Organization</li><li>Business Consulting</li><li>Event Planning</li><li>Travel Arrangements</li><li>Blast Mailings</li></ul>
  </div>
  <div class="f-col f-contact" style="left:489px">
    <h5>CONTACT US</h5>
    <ul>
      <li><svg width="9" height="11" viewBox="0 0 10 12"><path d="M5 12S0 7 0 4.5a5 5 0 0 1 10 0C10 7 5 12 5 12z" fill="#ddd"/></svg><span>P.O. Box 40218, Marlow Creek,<br>Texas 75090</span></li>
      <li><svg width="10" height="10" viewBox="0 0 24 24"><path fill="#ddd" d="M6.6 10.8a15 15 0 0 0 6.6 6.6l2.2-2.2c.3-.3.7-.4 1-.2 1.1.4 2.3.6 3.6.6.6 0 1 .4 1 1V20c0 .6-.4 1-1 1A17 17 0 0 1 3 4c0-.6.4-1 1-1h3.5c.6 0 1 .4 1 1 0 1.3.2 2.5.6 3.6.1.3 0 .7-.2 1z"/></svg><span>(555) 014 2290</span></li>
      <li><svg width="11" height="9" viewBox="0 0 12 9"><rect width="12" height="9" fill="#ddd"/><path d="M0 0l6 5 6-5" stroke="#1f1f1f" fill="none"/></svg><span>help@brimloop.biz</span></li>
    </ul>
  </div>
  <div class="f-col" style="left:702px">
    <h5>NEWSLETTER SIGNUP</h5>
    <div class="email-field"><svg width="11" height="9" viewBox="0 0 12 9"><rect width="12" height="9" fill="#ccc"/><path d="M0 0l6 5 6-5" stroke="#3a3a3a" fill="none"/></svg>E mail id</div>
    <div class="signup">SIGNUP!</div>
  </div>
  <div class="f-brand">BrimLoop</div>
  <div class="copyright">Copyright @ 2016 All Rights REserved</div>
</footer>

<div class="tribar bottom"><span class="g"></span><span class="r"></span><span class="t"></span></div>

</body>
</html>
```